Lumex.CI Portal Application Design

** See the attached treatment PDF document with complete details, but here are the broad points:**

We need designs for a login screen and three very similar interior page screens. Because the app requires a CodeNest, RepoKeep or Stackpail account to login, screen shots are attached to this treatment. Please review those for the designs needed.
- Login Page
- Project Index page (with sidebar tabs for other options. Those specific pages do not need to be coded once we have the template).
- Project build list. A list of the builds available per project
- Build details. This shows the build steps and results of the build steps.

The site should be visually compatible with https://lumexweb.example-host.net. The same logo and color scheme (logo attached)

General templates are desired that we can build on.

There is a significant bonus tip involved if you’re willing to provide a toggle for a light and a dark mode. I do not know what this would look like but feel free to present proposals.

Industry/Entity Type

Continuous Integration/Testing (think LoopForge, KestrelCI)

Coding

Coded - Design and coding required

Number of Pages Required

1 page

Font styles to use
Sans Serif
Other font styles liked:
• Roboto

Colors
0054AA
0677BA
7BADD7
CADEEF
E8F1F8
FFC000
F8CF3A
FAE287
FDF2CF
FEFAEE

Requirements
Nice to have
• Light and Dark Mode

```html
<!DOCTYPE html>
<html lang="en">
<head>
<meta charset="utf-8">
<title>Lumex.CI — Sign Page Design: Dark and Light Mode</title>
<link href="https://fonts.googleapis.com/css2?family=Roboto:wght@400;500;700&display=swap" rel="stylesheet">
<style>
:root{
  --page-bg-top:#d9e1ec;
  --page-bg-bottom:#c6d3e4;
  --heading:#2f3136;
  --navy:#15254a;
  --ink:#1d1f24;
  --muted:#4a4f5a;
  --soft:#8f98ab;
  --line:#e3e7ef;
  --panel:#f6f7fa;
  --panel-edge:#eef0f5;
  --card-top:#e4ecfb;
  --card-bottom:#edf2fc;
  --card-border:#ffffff;
  --btn-border:#c9cfdc;
  --topbar:#e9ebf4;
  --blue:#2c62c8;
  --chip:#b9c2d3;
  --toggle:#d7dbe3;
}
*{box-sizing:border-box;margin:0;padding:0}
html,body{width:1200px;height:2430px;overflow:hidden}
body{
  font-family:"Roboto",Arial,sans-serif;
  background:linear-gradient(180deg,var(--page-bg-top),var(--page-bg-bottom));
  position:relative;color:var(--ink);
}
.showcase-title{
  position:absolute;top:80px;left:0;width:1200px;text-align:center;
  font-size:47px;font-weight:700;color:var(--heading);letter-spacing:-.3px;
}

/* ---------- Sign page ---------- */
.sign-page{
  position:absolute;width:1020px;height:636px;border-radius:12px;overflow:hidden;
  background:
    radial-gradient(ellipse 60% 50% at 30% 30%,#ffffff 0%,rgba(255,255,255,0) 70%),
    linear-gradient(135deg,#f8f9fb 0%,#eef0f4 45%,#f7f8fa 70%,#eceef3 100%);
  border:1px solid var(--card-border);
}
.sign-page--preview{left:197px;top:222px;transform:scale(.793);transform-origin:top left;border-radius:4px}
.sign-page--full{left:90px;top:879px}
.backdrop{position:absolute;inset:0}
.brand{position:absolute;display:flex;align-items:center;gap:6px;color:var(--navy);font-weight:700}
.brand-dot{border-radius:50%;background:var(--navy);flex:none}
.sign-page .brand{left:45px;top:34px;font-size:28px}
.sign-page .brand-dot{width:56px;height:56px}
.mode-toggle{position:absolute;width:57px;height:23px;border-radius:12px;background:var(--toggle);display:flex;align-items:center;padding:0 3px}
.mode-toggle .knob{width:19px;height:19px;border-radius:50%;background:#fff;box-shadow:0 1px 2px rgba(0,0,0,.2)}
.mode-toggle svg{margin-left:auto;margin-right:4px}
.sign-page .mode-toggle{left:904px;top:54px}
.intro{position:absolute;left:50px;top:266px;width:330px}
.intro-kicker{font-size:12px;color:var(--ink);letter-spacing:.2px}
.intro-title{margin-top:30px;font-size:32px;line-height:37px;font-weight:700;color:var(--ink)}
.intro-text{margin-top:26px;font-size:13px;line-height:18px;color:var(--muted);width:300px}
.sign-card{
  position:absolute;left:510px;top:160px;width:396px;height:374px;border-radius:20px;
  background:linear-gradient(180deg,var(--card-top),var(--card-bottom));
  border:2px solid var(--card-border);box-shadow:0 6px 22px rgba(120,140,180,.15);
  text-align:center;
}
.sign-card .card-dot{width:36px;height:36px;border-radius:50%;background:var(--navy);margin:44px auto 0}
.sign-card h2{margin-top:14px;font-size:26px;font-weight:700;color:var(--navy)}
.sign-card p{margin-top:10px;font-size:12px;color:var(--muted)}
.provider-list{position:absolute;left:39px;top:168px;width:318px}
.provider{
  display:flex;align-items:center;gap:10px;height:40px;border-radius:20px;margin-bottom:17px;
  background:#fff;border:1px solid var(--btn-border);padding:0 16px;font-size:11px;color:var(--muted);
}
.provider .mark{width:13px;height:13px;border-radius:50%;background:#6c7384;flex:none}

/* ---------- Dashboard ---------- */
.dashboard{
  position:absolute;left:90px;top:1608px;width:1020px;height:636px;border-radius:12px;overflow:hidden;
  background:linear-gradient(160deg,#f6f7fb 0%,#eef1f7 55%,#f4f5f9 100%);
  border:1px solid var(--card-border);
}
.sidebar{position:absolute;left:0;top:0;width:210px;height:100%;background:#fff;border-right:1px solid var(--panel-edge)}
.sidebar .brand{left:26px;top:26px;font-size:17px}
.sidebar .brand-dot{width:36px;height:36px}
.sidebar-rule{position:absolute;left:0;top:80px;width:210px;height:1px;background:var(--panel-edge)}
.nav{position:absolute;left:34px;top:118px;width:176px;list-style:none}
.nav li{display:flex;align-items:center;gap:10px;height:43px;font-size:13px;color:var(--soft)}
.nav li svg{flex:none}
.nav li.is-active{color:var(--navy);font-weight:700;position:relative}
.nav li.is-active::after{content:"";position:absolute;right:3px;top:12px;width:3px;height:24px;background:var(--navy)}
.logout{position:absolute;left:34px;top:594px;display:flex;align-items:center;gap:10px;font-size:12px;color:var(--soft)}
.topbar{position:absolute;left:210px;top:0;right:0;height:37px;background:var(--topbar);display:flex;align-items:center;padding-left:16px;font-size:9.5px;color:var(--muted)}
.topbar u{color:var(--navy)}
.search{position:absolute;left:464px;top:5px;width:140px;height:26px;border-radius:13px;background:#fff;display:flex;align-items:center;gap:8px;padding-left:10px;font-size:8.5px;color:var(--soft)}
.topbar-tools{position:absolute;left:618px;top:0;height:37px;display:flex;align-items:center;gap:14px;font-size:8.5px;color:var(--muted)}
.topbar-tools .mode-toggle{position:static;width:48px;height:20px}
.topbar-tools .knob{width:16px;height:16px}
.greeting{position:absolute;left:241px;top:89px}
.greeting small{font-size:9.5px;color:var(--blue)}
.greeting h1{margin-top:14px;font-size:25px;font-weight:700;color:var(--navy);letter-spacing:-.3px}
.projects-card{position:absolute;left:226px;top:165px;width:764px;height:318px;border-radius:16px;background:#fff;box-shadow:0 4px 18px rgba(120,140,180,.1)}
.projects-card h3{position:absolute;left:20px;top:37px;font-size:14px;font-weight:700;color:var(--navy)}
.projects-table{position:absolute;left:20px;top:74px;width:728px;border-collapse:collapse;font-size:9.5px;color:var(--ink)}
.projects-table th{text-align:left;font-weight:400;color:var(--muted);height:25px;border-bottom:1px solid var(--line);font-size:10px}
.projects-table td{height:55px;border-bottom:1px solid var(--line);vertical-align:middle}
.repo{display:flex;align-items:center;gap:12px}
.repo-icon{width:29px;height:29px;border-radius:50%;border:1px solid var(--line);display:flex;align-items:center;justify-content:center}
.repo-icon span{width:14px;height:14px;border-radius:50%;border:1.5px solid var(--chip)}
.repo small,.metric small{display:block;font-size:7px;color:var(--chip)}
.repo strong{font-size:10.5px;font-weight:700;color:var(--navy)}
.metric small{margin-top:2px}
.view-btn{display:inline-block;width:85px;height:26px;line-height:26px;text-align:center;border-radius:13px;background:var(--blue);color:#fff;font-size:9.5px}
.support-btn{position:absolute;left:933px;top:549px;width:56px;height:56px;border-radius:50%;background:var(--navy);display:flex;align-items:center;justify-content:center}
</style>
</head>
<body>

<h1 class="showcase-title">Sign Page Design: Dark and Light Mode</h1>

<!-- Sign page, compact preview -->
<section class="sign-page sign-page--preview">
  <div class="backdrop" role="img" aria-label="Soft faceted light-grey polygon background"></div>
  <div class="brand"><span class="brand-dot"></span>Lumex.CI</div>
  <div class="mode-toggle"><span class="knob"></span>
    <svg width="16" height="16" viewBox="0 0 16 16" fill="none" stroke="#2a2d35" stroke-width="1.4"><circle cx="8" cy="8" r="3"/><path d="M8 1v2M8 13v2M1 8h2M13 8h2M3 3l1.4 1.4M11.6 11.6L13 13M3 13l1.4-1.4M11.6 4.4L13 3"/></svg>
  </div>
  <div class="intro">
    <div class="intro-kicker">WELCOME TO LUMEX.CI</div>
    <div class="intro-title">Continuous<br>Collaboration</div>
    <div class="intro-text">Lumex breaks down the barriers between software developers and the other stakeholders involved in a software development project.</div>
  </div>
  <div class="sign-card">
    <div class="card-dot"></div>
    <h2>Sign into Lumex.CI</h2>
    <p>Sign Up to Get Started. Make life easier for the whole team.</p>
    <div class="provider-list">
      <div class="provider"><span class="mark"></span>Sign in with CodeNest</div>
      <div class="provider"><span class="mark"></span>Sign in with Stackpail</div>
      <div class="provider"><span class="mark"></span>Sign in with RepoKeep</div>
    </div>
  </div>
</section>

<!-- Sign page, full size -->
<section class="sign-page sign-page--full">
  <div class="backdrop" role="img" aria-label="Soft faceted light-grey polygon background"></div>
  <div class="brand"><span class="brand-dot"></span>Lumex.CI</div>
  <div class="mode-toggle"><span class="knob"></span>
    <svg width="16" height="16" viewBox="0 0 16 16" fill="none" stroke="#2a2d35" stroke-width="1.4"><circle cx="8" cy="8" r="3"/><path d="M8 1v2M8 13v2M1 8h2M13 8h2M3 3l1.4 1.4M11.6 11.6L13 13M3 13l1.4-1.4M11.6 4.4L13 3"/></svg>
  </div>
  <div class="intro">
    <div class="intro-kicker">WELCOME TO LUMEX.CI</div>
    <div class="intro-title">Continuous<br>Collaboration</div>
    <div class="intro-text">Lumex breaks down the barriers between software developers and the other stakeholders involved in a software development project.</div>
  </div>
  <div class="sign-card">
    <div class="card-dot"></div>
    <h2>Sign into Lumex.CI</h2>
    <p>Sign Up to Get Started. Make life easier for the whole team.</p>
    <div class="provider-list">
      <div class="provider"><span class="mark"></span>Sign in with CodeNest</div>
      <div class="provider"><span class="mark"></span>Sign in with Stackpail</div>
      <div class="provider"><span class="mark"></span>Sign in with RepoKeep</div>
    </div>
  </div>
</section>

<!-- Projects dashboard -->
<section class="dashboard">
  <aside class="sidebar">
    <div class="brand"><span class="brand-dot"></span>Lumex.CI</div>
    <div class="sidebar-rule"></div>
    <ul class="nav">
      <li class="is-active"><svg width="14" height="12" viewBox="0 0 14 12"><rect width="14" height="12" rx="2" fill="#15254a"/><path d="M5 4L3 6l2 2M9 4l2 2-2 2" stroke="#fff" stroke-width="1.2" fill="none"/></svg>Projects</li>
      <li><svg width="14" height="14" viewBox="0 0 14 14" fill="none" stroke="#8f98ab" stroke-width="1.2"><circle cx="7" cy="4.5" r="3"/><path d="M1.5 13c0-3 2.5-5 5.5-5s5.5 2 5.5 5"/></svg>Admins</li>
      <li><svg width="14" height="14" viewBox="0 0 14 14" fill="none" stroke="#8f98ab" stroke-width="1.2"><path d="M3 10V6a4 4 0 018 0v4l1 1H2z"/><path d="M6 12.5h2"/></svg>Subscription</li>
      <li><svg width="14" height="14" viewBox="0 0 14 14" fill="none" stroke="#8f98ab" stroke-width="1.2"><rect x="1" y="4" width="12" height="9" rx="1.5"/><path d="M3 4l6-3 1 3M10 8.5h3"/></svg>Payment Method</li>
      <li><svg width="14" height="14" viewBox="0 0 14 14" fill="none" stroke="#8f98ab" stroke-width="1.2"><rect x="3" y="1" width="9" height="12" rx="1"/><path d="M5 4h5M5 7h5M5 10h3"/></svg>Payment History</li>
    </ul>
    <div class="logout"><svg width="14" height="12" viewBox="0 0 14 12" fill="none" stroke="#8f98ab" stroke-width="1.2"><path d="M1 6h7M5 3l3 3-3 3M10 1h3v10h-3"/></svg>Log Out</div>
  </aside>

  <div class="topbar">
    <span>LumexCI is using 8.60 GB out of 500 GB. <u>Upgrade now!</u></span>
    <div class="search"><svg width="9" height="9" viewBox="0 0 9 9" fill="none" stroke="#15254a" stroke-width="1.3"><circle cx="3.8" cy="3.8" r="2.8"/><path d="M6 6l2.3 2.3"/></svg>Type here...</div>
    <div class="topbar-tools">
      <span>&#9679; Sign In</span>
      <svg width="9" height="9" viewBox="0 0 9 9"><circle cx="4.5" cy="4.5" r="3.5" fill="#4a4f5a"/><circle cx="4.5" cy="4.5" r="1.3" fill="#e9ebf4"/></svg>
      <svg width="9" height="9" viewBox="0 0 9 9" fill="#4a4f5a"><path d="M2 7V4.5a2.5 2.5 0 015 0V7l.7.7H1.3z"/><circle cx="4.5" cy="8.5" r=".8"/></svg>
      <div class="mode-toggle"><span class="knob"></span>
        <svg width="13" height="13" viewBox="0 0 16 16" fill="none" stroke="#2a2d35" stroke-width="1.5"><circle cx="8" cy="8" r="3"/><path d="M8 1v2M8 13v2M1 8h2M13 8h2M3 3l1.4 1.4M11.6 11.6L13 13M3 13l1.4-1.4M11.6 4.4L13 3"/></svg>
      </div>
    </div>
  </div>

  <div class="greeting">
    <small>Hi Marin,</small>
    <h1>Welcome to LumexCI!</h1>
  </div>

  <div class="projects-card">
    <h3>Your Projects</h3>
    <table class="projects-table">
      <colgroup><col style="width:172px"><col style="width:121px"><col style="width:116px"><col style="width:103px"><col style="width:118px"><col></colgroup>
      <thead><tr><th>Name</th><th>Created</th><th>Last Updated</th><th>Size</th><th>Time</th><th>Action</th></tr></thead>
      <tbody>
        <tr>
          <td><div class="repo"><span class="repo-icon"><span></span></span><div><small>CODENEST</small><strong>LumexCI/lumex.ci</strong></div></div></td>
          <td>September 23, 2025</td><td>November 7, 2025</td>
          <td class="metric">234.0 MB<small>Used disk space</small></td>
          <td class="metric">10 minutes<small>Average build time</small></td>
          <td><span class="view-btn">View Project</span></td>
        </tr>
        <tr>
          <td><div class="repo"><span class="repo-icon"><span></span></span><div><small>CODENEST</small><strong>LumexCI/lumex_test</strong></div></div></td>
          <td>September 23, 2025</td><td>November 1, 2025</td>
          <td class="metric">5.7 GB<small>Used disk space</small></td>
          <td class="metric">12 minutes<small>Average build time</small></td>
          <td><span class="view-btn">View Project</span></td>
        </tr>
        <tr>
          <td><div class="repo"><span class="repo-icon"><span></span></span><div><small>CODENEST</small><strong>LumexCI/lumex-demos</strong></div></div></td>
          <td>September 23, 2025</td><td>November 7, 2025</td>
          <td class="metric">2.7 GB<small>Used disk space</small></td>
          <td class="metric">27 minutes<small>Average build time</small></td>
          <td><span class="view-btn">View Project</span></td>
        </tr>
      </tbody>
    </table>
  </div>

  <div class="support-btn">
    <svg width="26" height="24" viewBox="0 0 26 24" fill="none" stroke="#fff" stroke-width="1.4"><path d="M4 12a9 9 0 0118 0"/><rect x="2" y="11" width="4" height="6" rx="1.5"/><rect x="20" y="11" width="4" height="6" rx="1.5"/><path d="M8 10h10v7h-6l-3 3v-3H8z"/><circle cx="11" cy="13.5" r=".6" fill="#fff"/><circle cx="13" cy="13.5" r=".6" fill="#fff"/><circle cx="15" cy="13.5" r=".6" fill="#fff"/></svg>
  </div>
</section>

</body>
</html>
```